Soccer Club Site Redesign

We are a suburban youth soccer club in need of a web site redesign. Our current site’s look/feel is outdated and is in need of a more modern look. What we are looking for is a design layout that will accommodate the current functionality we have for the site and give us an updated modern look. The deliverable for this project will be .psd file that can be converted to an html theme file for Wordpress. We will take care of the conversion and handle the html coding/javascript functionality.
Take a look at our current site to get an idea of what we offer and the current layout we have.
http://www.torvelkicks.org
Our club hosts youth recreational soccer, traveling soccer and two large soccer tournaments during the year. We also sponsor a number of training clinics. Our site serves a couple primary purposes:
1. Parents learn how/where/when to sign up their child for the leagues we offer.
2. Parents learn dates/times of various events the club offers.
3. Other soccer clubs get information on the tournaments we offer, sign up for the tournaments etc.
We do a pretty good job of presenting information about the various events/leagues available and how to sign up for them, but we want to do a better job of presenting a calendar where parents can quickly find dates/times of various events. Ideally, we would like to incorporate a news section (like we currently have), with a calendar and the use of more images on the home page. We understand screen space is limited but would incorporate jquery/javascript widgets to hide/show info and maybe an ‘imagebox’ for the additional images.
Here are a few sites with ideas that we liked:
http://sports.brenwickcollege.edu/ (Look at the Upcoming Events calendar on the page)
http://www.fennlowfutbol.com/ (look at the Upcoming Events calendar in the right column and the image box in the main content area)
http://www.rundlekick.com/index.php (Like the look and use of images)
http://www.qvfootyclub.com/ (imagebox use)
http://www.sarvapuckclub.org/ ( hockey website but like the use of crisp header graphics)
http://www.delvingpuckers.com/ (another hockey site, like the calendar used)
That should give you a pretty good idea of what we are looking for. The new design will need to accommodate the existing functionality of the site. Our logo (which is attached) should be incorporated into the site….otherwise we are open to your design ideas.

```html
<!DOCTYPE html>
<html lang="en">
<head>
<meta charset="utf-8">
<title>Torvel Soccer Club</title>
<link href="https://fonts.googleapis.com/css2?family=Source+Sans+3:wght@400;600;700&family=Open+Sans:wght@400;600&display=swap" rel="stylesheet">
<style>
:root{
  --navy:#2b2d9b;
  --navy-deep:#1f1f86;
  --orange:#f7b200;
  --orange-light:#ffd24a;
  --orange-text:#d99400;
  --text:#222;
  --muted:#6e6e6e;
  --soft:#9a9a9a;
  --panel:#f2f2f2;
  --footer:#2d2d2d;
  --banner-a:#0b6fb0;
  --banner-b:#2aa3dc;
}
*{box-sizing:border-box;margin:0;padding:0}
html,body{width:1200px;height:1089px;overflow:hidden}
body{font-family:"Source Sans 3",sans-serif;background:var(--navy-deep)}
.stage{position:relative;width:1300px;height:1180px;transform:scale(0.92308);transform-origin:0 0;
  background:linear-gradient(90deg,#2a2aa6 0%,#3535b8 12%,#2b2ba8 100%)}
.topline{position:absolute;left:0;top:0;width:1300px;height:11px;background:#c7c9c8}
.side-art{position:absolute;top:11px;height:560px;background:radial-gradient(ellipse at center,rgba(140,150,235,.45),rgba(60,60,180,0) 70%)}
.side-art.left{left:0;width:160px}
.side-art.right{left:1141px;width:159px}
.page{position:absolute;left:160px;top:11px;width:981px;height:1169px;background:#fff}
.masthead{position:absolute;left:0;top:0;width:981px;height:107px;background:linear-gradient(90deg,#fff 0%,#f1f1f1 40%,#e4e4e4 70%,#f4f4f4 100%)}
.brand{position:absolute;left:30px;top:30px;display:flex;align-items:center;gap:10px;font-weight:700;font-size:22px;color:var(--navy)}
.brand-dot{width:38px;height:38px;border-radius:50%;background:var(--navy)}
.search{position:absolute;left:767px;top:22px;width:188px;height:23px;background:#fff;border:1px solid #cfcfcf;box-shadow:inset 0 1px 2px rgba(0,0,0,.1);font-style:italic;font-size:11px;color:#aaa;padding:4px 16px;display:flex;justify-content:space-between;align-items:center}
.nav{position:absolute;left:2px;top:107px;width:978px;height:46px;background:linear-gradient(#fcc31a,#f4a900);display:flex;border-bottom:1px solid #e19a00}
.nav a{height:46px;display:flex;align-items:center;justify-content:center;font-size:14px;color:#2a2a2a;text-decoration:none;border-right:1px solid #e39f00;box-shadow:1px 0 0 #ffd35c}
.nav a.active{background:linear-gradient(#ffd63a,#fcc313)}
.hero{position:absolute;left:6px;top:162px;width:969px;height:277px;background:#2a2a2a;overflow:hidden}
.hero-photo{position:absolute;left:0;top:0;width:725px;height:277px;background:radial-gradient(ellipse at 30% 45%,#3f5f85 0%,#2c2620 45%,#1d1712 100%)}
.hero-title{position:absolute;left:412px;top:114px;font-family:"Open Sans",sans-serif;font-size:30px;color:#fff;letter-spacing:.5px}
.dots{position:absolute;left:592px;top:243px;display:flex;gap:11px}
.dots span{width:10px;height:10px;border-radius:50%;background:#cfcfcf}
.dots span:first-child{background:var(--orange)}
.schedule{position:absolute;left:726px;top:6px;width:237px;height:263px;background:#fff;border-radius:3px;overflow:hidden}
.schedule h2{height:40px;background:linear-gradient(#ffce2a,#f3ad00);font-weight:400;font-size:17px;color:#333;padding:11px 17px;font-family:"Open Sans",sans-serif}
.event{display:flex;gap:14px;padding:12px 12px 0 13px;height:64.5px}
.cal{width:36px;text-align:center;font-size:9.5px;color:var(--navy);font-family:"Open Sans",sans-serif}
.cal svg{display:block;margin:0 auto 2px}
.event h3{font-weight:400;font-size:12px;color:var(--orange-text);font-family:"Open Sans",sans-serif;margin-bottom:3px}
.event p{font-size:10px;color:#666;line-height:14px;font-family:"Open Sans",sans-serif}
.schedule .more{position:absolute;left:0;bottom:0;width:237px;height:26px;background:#eee;font-size:10px;color:#555;text-align:center;line-height:26px;font-family:"Open Sans",sans-serif}
.welcome{position:absolute;left:6px;top:467px;width:590px}
.welcome h1{font-weight:600;font-size:23px;color:var(--navy);margin-bottom:14px}
.welcome .lead{font-size:12.5px;color:var(--text);line-height:22px;margin-bottom:8px}
.welcome .body{font-size:12.5px;color:var(--muted);line-height:22px;text-align:justify}
.btn{position:absolute;left:-1px;top:239px;width:93px;height:29px;border-radius:15px;background:linear-gradient(#5a5a5a,#333);color:#fff;font-size:12.5px;display:flex;align-items:center;justify-content:center;box-shadow:0 2px 3px rgba(0,0,0,.25)}
.promo{position:absolute;left:616px;width:358px;height:129px;background:linear-gradient(90deg,var(--banner-a),var(--banner-b));overflow:hidden}
.promo.one{top:471px}
.promo.two{top:612px}
.promo-art{position:absolute;right:0;top:0;width:150px;height:129px;background:radial-gradient(circle at 55% 50%,rgba(255,255,255,.55),rgba(255,255,255,0) 60%)}
.promo-text{position:absolute;left:17px;top:18px;font-weight:600;color:#fdc11a;font-size:17px;line-height:30px}
.promo-text .club{color:#fff;padding-left:22px;font-weight:400;font-size:17px}
.promo-text .club b{font-weight:700;font-size:26px}
.cols{position:absolute;left:6px;top:763px;display:flex;gap:12px}
.col{width:315px;height:217px;background:var(--panel)}
.col:nth-child(3){width:315px}
.col h2{font-weight:600;font-size:18px;color:var(--navy);padding:9px 10px 0;height:42px;border-bottom:1px solid #e2e2e2}
.item{display:flex;gap:14px;padding:20px 11px 0}
.thumb{flex:none;width:64px;height:58px;border:1px solid #bcbcbc;padding:2px;background:#fff}
.thumb div{width:100%;height:100%}
.item p{font-size:13px;color:#555;line-height:20px}
.item small{font-size:11px;color:var(--soft);display:block}
.partners{position:absolute;left:6px;top:987px;width:969px;height:98px;border-top:1px solid #e5e5e5;display:flex;justify-content:space-around;align-items:center;padding:0 12px}
.badge{background:#c6c6c6}
.footer{position:absolute;left:0;top:1085px;width:981px;height:84px;background:var(--footer);color:#ddd;font-size:12.5px}
.footer nav{position:absolute;left:14px;top:20px;display:flex}
.footer nav a{color:#ddd;text-decoration:none}
.footer nav span{color:#777;padding:0 9px}
.copy{position:absolute;left:14px;top:50px}
.social{position:absolute;right:13px;top:28px;display:flex;gap:7px}
.social span{width:30px;height:30px;border-radius:50%;background:#fff}
</style>
</head>
<body>
<div class="stage">
  <div class="topline"></div>
  <div class="side-art left" role="img" aria-label="Faint blue-toned soccer ball backdrop"></div>
  <div class="side-art right" role="img" aria-label="Faint blue-toned player action backdrop"></div>

  <div class="page">
    <header class="masthead" role="img" aria-label="Soft grey stadium pitch lines">
      <div class="brand"><span class="brand-dot"></span>Torvel Soccer Club</div>
      <div class="search"><span>Search</span>
        <svg width="10" height="10" viewBox="0 0 10 10"><circle cx="4" cy="4" r="3" fill="none" stroke="#aaa" stroke-width="1.4"/><line x1="6.2" y1="6.2" x2="9.3" y2="9.3" stroke="#aaa" stroke-width="1.6"/></svg>
      </div>
    </header>

    <nav class="nav">
      <a class="active" style="width:81px">Home</a>
      <a style="width:92px">About us</a>
      <a style="width:72px">Forms</a>
      <a style="width:88px">Calender</a>
      <a style="width:89px">Traveling</a>
      <a style="width:109px">Recreational</a>
      <a style="width:113px">Tournaments</a>
      <a style="width:99px">Field Maps</a>
      <a style="width:78px">People</a>
      <a style="width:83px">Contact</a>
      <a style="width:74px;border:0;box-shadow:none">Links</a>
    </nav>

    <section class="hero">
      <div class="hero-photo" role="img" aria-label="Player in blue kit striking a ball under stadium lights"></div>
      <div class="hero-title">Contantry Popular</div>
      <div class="dots"><span></span><span></span><span></span><span></span></div>
      <aside class="schedule">
        <h2>Upcoming Schedule</h2>
        <div class="event"><div class="cal"><svg width="28" height="26" viewBox="0 0 28 26"><rect x="1" y="3" width="26" height="22" rx="2" fill="#fff" stroke="#2b2d9b" stroke-width="2"/><rect x="1" y="3" width="26" height="6" fill="#2b2d9b"/><rect x="7" y="0" width="3" height="6" fill="#2b2d9b"/><rect x="18" y="0" width="3" height="6" fill="#2b2d9b"/><text x="14" y="21" text-anchor="middle" font-size="11" font-weight="700" fill="#2b2d9b" font-family="Open Sans,sans-serif">17</text></svg>October</div>
          <div><h3>DRYSA Bingo - Linden</h3><p>6:30pm-8:30pm (CDT)<br>Bingo at Linden Hall</p></div></div>
        <div class="event"><div class="cal"><svg width="28" height="26" viewBox="0 0 28 26"><rect x="1" y="3" width="26" height="22" rx="2" fill="#fff" stroke="#2b2d9b" stroke-width="2"/><rect x="1" y="3" width="26" height="6" fill="#2b2d9b"/><rect x="7" y="0" width="3" height="6" fill="#2b2d9b"/><rect x="18" y="0" width="3" height="6" fill="#2b2d9b"/><text x="14" y="21" text-anchor="middle" font-size="11" font-weight="700" fill="#2b2d9b" font-family="Open Sans,sans-serif">17</text></svg>October</div>
          <div><h3>DRYSA Bingo - Linden</h3><p>6:30pm-8:30pm (CDT)<br>Bingo at Linden Hall</p></div></div>
        <div class="event"><div class="cal"><svg width="28" height="26" viewBox="0 0 28 26"><rect x="1" y="3" width="26" height="22" rx="2" fill="#fff" stroke="#2b2d9b" stroke-width="2"/><rect x="1" y="3" width="26" height="6" fill="#2b2d9b"/><rect x="7" y="0" width="3" height="6" fill="#2b2d9b"/><rect x="18" y="0" width="3" height="6" fill="#2b2d9b"/><text x="14" y="21" text-anchor="middle" font-size="11" font-weight="700" fill="#2b2d9b" font-family="Open Sans,sans-serif">17</text></svg>October</div>
          <div><h3>DRYSA Bingo - Linden</h3><p>6:30pm-8:30pm (CDT)<br>Bingo at Linden Hall</p></div></div>
        <div class="more">View more &gt;&gt;</div>
      </aside>
    </section>

    <section class="welcome">
      <h1>Welcome to Torvel Soccer Club</h1>
      <p class="lead">Sed ut perspiciatis unde omnis iste natus error sit voluptatem accusantium doloremque laudan tium, totam rem aperiam, eaque ipsa quae ab illo inventore veritatis.</p>
      <p class="body">Nemo enim ipsam voluptatem quia voluptas sit aspernatur aut odit aut fugit, sed quia consequuntur magni dolores eos qui ratione voluptatem sequi nesciunt. Neque porro quisquam est, qui dolorem ipsum quia dolor sit amet, consectetur, adipisci velit, sed quia non numquam eius modi tempora incidunt ut labore et dolore magnam aliquam quaerat voluptatem. Ut enim ad minima veniam, quis nostrum exercitationem ullam corporis suscipit laboriosam, nisi ut aliquid ex ea commodi conse quatur. Quis autem vel eum iure reprehen derit qui in ea voluptate velit esse quam nihil molestiae consequatur.</p>
      <div class="btn">View more</div>
    </section>

    <a class="promo one">
      <div class="promo-art" role="img" aria-label="Soccer ball caught in goal net"></div>
      <div class="promo-text">View recent<div class="club"><b>Torvel</b> Soccer Club's</div>Matches</div>
    </a>
    <a class="promo two">
      <div class="promo-art" role="img" aria-label="Silver trophy cup"></div>
      <div class="promo-text">View recent<div class="club"><b>Torvel</b> Soccer Club's</div>Trophy</div>
    </a>

    <section class="cols">
      <div class="col"><h2>Latest News</h2>
        <div class="item"><div class="thumb"><div role="img" aria-label="Youth players on the pitch" style="background:linear-gradient(#6f8a6a,#4e6b4a)"></div></div><p>Neque porro pandr quisquam est, qui dolorem ipsum quia.<small>October 30th, 2012</small></p></div>
        <div class="item"><div class="thumb"><div role="img" aria-label="Soccer ball on grass" style="background:linear-gradient(#9fb6d6,#5f7fa6)"></div></div><p>Neque porro pandr quisquam est, qui dolorem ipsum quia.<small>October 30th, 2012</small></p></div>
      </div>
      <div class="col"><h2>Latest Events</h2>
        <div class="item"><div class="thumb"><div role="img" aria-label="Children playing a match" style="background:linear-gradient(#7fae6a,#4f7f3e)"></div></div><p>Neque porro pandr quisquam est, qui dolorem ipsum quia.<small>October 30th, 2012</small></p></div>
        <div class="item"><div class="thumb"><div role="img" aria-label="Team in red shirts" style="background:linear-gradient(#c9615a,#8e3a34)"></div></div><p>Neque porro pandr quisquam est, qui dolorem ipsum quia.<small>October 30th, 2012</small></p></div>
      </div>
      <div class="col"><h2>Our Coaches</h2>
        <div class="item"><div class="thumb"><div role="img" aria-label="Coach on the field" style="background:linear-gradient(#8aa36f,#5c7349)"></div></div><p>Neque porro pandr quisquam est, qui dolorem ipsum quia.<small>October 30th, 2012</small></p></div>
        <div class="item"><div class="thumb"><div role="img" aria-label="Coach portrait" style="background:linear-gradient(#9c8a7a,#5e5048)"></div></div><p>Neque porro pandr quisquam est, qui dolorem ipsum quia.<small>October 30th, 2012</small></p></div>
      </div>
    </section>

    <section class="partners" aria-label="Partner organisations">
      <div class="badge" style="width:56px;height:52px;border-radius:6px"></div>
      <div class="badge" style="width:84px;height:40px;border-radius:20px"></div>
      <div class="badge" style="width:54px;height:44px;border-radius:8px"></div>
      <div class="badge" style="width:38px;height:44px;border-radius:4px 4px 19px 19px"></div>
      <div class="badge" style="width:58px;height:46px;border-radius:50%"></div>
      <div class="badge" style="width:89px;height:42px;border-radius:3px"></div>
      <div class="badge" style="width:64px;height:46px;border-radius:6px"></div>
      <div class="badge" style="width:56px;height:52px;border-radius:6px"></div>
    </section>

    <footer class="footer">
      <nav><a>Home</a><span>|</span><a>About us</a><span>|</span><a>Forms</a><span>|</span><a>Calender</a><span>|</span><a>Traveling</a><span>|</span><a>Recreational</a><span>|</span><a>Tournaments</a><span>|</span><a>Field Maps</a><span>|</span><a>People</a><span>|</span><a>Contact</a><span>|</span><a>Links</a></nav>
      <div class="copy">Copyright © 2012 www.torvelkicks.org &nbsp;&nbsp;&nbsp;&nbsp;All rights reserved.</div>
      <div class="social"><span aria-label="Social profile"></span><span aria-label="Social feed"></span></div>
    </footer>
  </div>
</div>
</body>
</html>
```